Business Card Design Project

We require a professional business card designed for our consulting organisation that has the same theme and colours as our logo except for the grey.

Colours on the front should predominately be white however some reference to our logo colours except for the grey.

The back of the card should be have background colour that aligns with our logo colour.

Layout, style and design is up to the designer. So send through your designs

Details are attached in the word document project brief.

Target Market(s)

Target market are large corporate organisations

Industry/Entity Type

Business

Requirements
Must have
• Content on the front must have:

Dean Halvorsen
Managing Director

P: 0417 285 394
E: Dean@brevolinkpartners.com
W: www.brevolinkpartners.com

Content on the back must have the words:
Alliances
Placement
Training
Support

Design Colours
Must align to our logo

```html
<!DOCTYPE html>
<html lang="en">
<head>
<meta charset="utf-8">
<title>BrevoLink Partners – Business Card</title>
<link rel="stylesheet" href="https://fonts.googleapis.com/css2?family=Open+Sans:wght@400;600;700&family=Roboto+Condensed:wght@400;700&display=swap">
<style>
  :root {
    --stage: #2a2a2a;
    --white: #ffffff;
    --paper: #f4f7fb;
    --blue-deep: #1168b8;
    --blue-mid: #1a86d0;
    --blue-light: #2aa6e0;
    --blue-ink: #1a73c4;
  }
  * { box-sizing: border-box; margin: 0; padding: 0; }
  html, body {
    width: 1200px; height: 900px; overflow: hidden;
    background: var(--stage);
    font-family: "Open Sans", Arial, sans-serif;
  }
  .canvas {
    position: relative; width: 1200px; height: 900px;
  }
  .card {
    position: absolute; top: 291px;
    width: 520px; height: 318px;
    overflow: hidden;
    box-shadow: 0 10px 30px rgba(0,0,0,.45);
  }
  .card--front { left: 60px; background: var(--paper); }
  .card--back {
    left: 620px;
    background: radial-gradient(ellipse at 35% 30%, var(--blue-mid) 0%, var(--blue-deep) 75%);
  }

  /* front */
  .front__band {
    position: absolute; left: 0; right: 0; top: 140px; bottom: 0;
    background: linear-gradient(160deg, var(--blue-mid) 0%, var(--blue-deep) 80%);
  }
  .front__band-accent {
    position: absolute; right: 0; top: 140px; width: 180px; bottom: 0;
    background: linear-gradient(200deg, rgba(42,166,224,.45), rgba(42,166,224,0) 70%);
  }
  .wordmark {
    position: absolute; display: flex; align-items: center; gap: 12px;
  }
  .wordmark__dot {
    width: 44px; height: 44px; border-radius: 50%; flex: none;
  }
  .wordmark__name {
    font-weight: 700; letter-spacing: 3px; line-height: 1.05; font-size: 22px;
  }
  .card--front .wordmark { left: 30px; top: 62px; }
  .card--front .wordmark__dot { background: var(--blue-ink); }
  .card--front .wordmark__name { color: var(--blue-ink); }

  .person {
    position: absolute; right: 26px; top: 108px; text-align: left;
    font-family: "Roboto Condensed", Arial, sans-serif;
  }
  .person__name { color: var(--blue-ink); font-weight: 700; font-size: 24px; line-height: 30px; }
  .person__role { color: var(--white); font-size: 15px; margin-top: 6px; padding-left: 30px; }

  .contact {
    position: absolute; left: 32px; bottom: 26px; list-style: none;
    color: var(--white); font-size: 13px; line-height: 22px;
  }
  .contact li { display: flex; align-items: center; gap: 12px; }
  .contact svg { width: 14px; height: 14px; flex: none; }
  .contact .spacer { width: 14px; }

  /* back */
  .back__glow {
    position: absolute; right: -60px; top: 40px; width: 300px; height: 320px;
    background: radial-gradient(ellipse at 60% 50%, rgba(42,166,224,.55), rgba(42,166,224,0) 70%);
  }
  .card--back .wordmark { left: 34px; top: 54px; }
  .card--back .wordmark__dot { background: var(--white); }
  .card--back .wordmark__name { color: var(--white); font-size: 24px; }

  .services {
    position: absolute; left: 40px; top: 186px; list-style: none;
    color: var(--white); font-weight: 600; font-size: 16px; line-height: 27px;
  }
  .services li { display: flex; align-items: center; gap: 14px; }
  .services svg { width: 18px; height: 16px; flex: none; }
</style>
</head>
<body>
<main class="canvas">

  <section class="card card--front" aria-label="Business card front">
    <div class="front__band"></div>
    <div class="front__band-accent"></div>

    <div class="wordmark">
      <span class="wordmark__dot"></span>
      <span class="wordmark__name">BrevoLink<br>Partners</span>
    </div>

    <div class="person">
      <p class="person__name">Dean Halvorsen</p>
      <p class="person__role">Managing Director</p>
    </div>

    <ul class="contact">
      <li>
        <svg viewBox="0 0 24 24" aria-hidden="true"><path fill="#fff" d="M6.6 10.8a15 15 0 0 0 6.6 6.6l2.2-2.2c.3-.3.7-.4 1-.2 1.1.4 2.3.6 3.6.6.6 0 1 .4 1 1V20c0 .6-.4 1-1 1A17 17 0 0 1 3 4c0-.6.4-1 1-1h3.5c.6 0 1 .4 1 1 0 1.3.2 2.5.6 3.6.1.3 0 .7-.2 1z"/></svg>
        <span>0417 285 394</span>
      </li>
      <li>
        <svg viewBox="0 0 24 24" aria-hidden="true"><path fill="#fff" d="M2 6h20v12H2z"/><path fill="none" stroke="#1a86d0" stroke-width="2" d="M2 6l10 7 10-7"/></svg>
        <span>Dean@brevolinkpartners.com</span>
      </li>
      <li>
        <span class="spacer"></span>
        <span>www.brevolinkpartners.com</span>
      </li>
    </ul>
  </section>

  <section class="card card--back" aria-label="Business card back">
    <div class="back__glow"></div>

    <div class="wordmark">
      <span class="wordmark__dot"></span>
      <span class="wordmark__name">BrevoLink<br>Partners</span>
    </div>

    <ul class="services">
      <li><svg viewBox="0 0 18 16" aria-hidden="true"><path fill="none" stroke="#fff" stroke-width="3" stroke-linecap="round" stroke-linejoin="round" d="M2 9l5 5L16 2"/></svg>Alliances</li>
      <li><svg viewBox="0 0 18 16" aria-hidden="true"><path fill="none" stroke="#fff" stroke-width="3" stroke-linecap="round" stroke-linejoin="round" d="M2 9l5 5L16 2"/></svg>Placement</li>
      <li><svg viewBox="0 0 18 16" aria-hidden="true"><path fill="none" stroke="#fff" stroke-width="3" stroke-linecap="round" stroke-linejoin="round" d="M2 9l5 5L16 2"/></svg>Training</li>
      <li><svg viewBox="0 0 18 16" aria-hidden="true"><path fill="none" stroke="#fff" stroke-width="3" stroke-linecap="round" stroke-linejoin="round" d="M2 9l5 5L16 2"/></svg>Support</li>
    </ul>
  </section>

</main>
</body>
</html>
```